Re-design of 4 x 2-sided reports

I need the 4 attached reports (3 are 2-sides of A4; 1 is 7-sides of A4) to be re-designed with a consistent look and feel. Just need 1 or 2 images per report being inserted plus consistent branding and contact details being displayed in the same location on each report with same colour, font and design). Reports are attached.
The reports are used as lead magnets.
That is, visitors to our website can download one of them (7 Steps To Sharpen Your Sales Pitch Before Spring Arrives) by filling in a form with their email address. Then over the next 30 days the other reports are sent to the subscriber via email autoresponders.
Blue Harbour Marketing is a marketing consultancy dealing with companies in the North West of England providing cost-effective and profitable marketing to small and medium-sized businesses that want better and quicker results. The reports need to be professional and corporate looking. Please let me know if you need any further clarification or have any questions. I attach an example report. I don't necessarily want to mirror this report (from the law firm) but it may help to understand what look I'm trying to get. Many thanks, Gordon

Target Market(s)

SMEs based in NW of England
Typically with turnover of £1m to £10m or 10 to 100 employees
Clients often in the construction sector, healthcare, accountants, lawyers and local councils.

Industry/Entity Type

Marketing

Font styles to use
Serif
Sans Serif

Colors
ec1f27

Requirements
Must have
• Consistent branding
• Logo in same place across all four reports
• Contact details in same place across all four reports
• Same font across all four reports
• Same colour across all four reports
• Professional and bold look
Nice to have
• Some strong stock photography
• 1 or 2 images per report
• More images for the 7-page report though
Should not have
• No graphics

```html
<!DOCTYPE html>
<html lang="en">
<head>
<meta charset="utf-8">
<title>7 Steps To Sharpen Your Sales Pitch Before Spring Arrives – Blue Harbour Marketing</title>
<link rel="stylesheet" href="https://fonts.googleapis.com/css2?family=Oswald:wght@500;700&family=Open+Sans:ital,wght@0,400;0,600;1,400&display=swap">
<style>
  :root {
    --brand-red: #ec1f27;
    --deep-red: #b3121a;
    --ink: #1a1a1a;
    --body-ink: #2b2b2b;
    --paper: #ffffff;
    --spine-grey: #e6e6e6;
    --backdrop: #d6d6d6;
    --rule: #9a9a9a;
  }
  * { box-sizing: border-box; margin: 0; padding: 0; }
  html, body { width: 1200px; height: 960px; overflow: hidden; }
  body {
    background: var(--backdrop);
    font-family: "Open Sans", Arial, sans-serif;
    color: var(--body-ink);
    position: relative;
  }
  .spread {
    position: absolute;
    left: 20px; top: 67px;
    width: 1160px; height: 826px;
    display: flex;
  }
  .page {
    position: relative;
    width: 580px; height: 826px;
    overflow: hidden;
  }
  .page--left { background: linear-gradient(90deg, var(--paper) 55%, var(--spine-grey) 100%); }
  .page--right { background: linear-gradient(90deg, #f1f1f1 0%, var(--paper) 12%); }

  /* Cover header */
  .cover { position: absolute; left: 0; top: 0; width: 580px; height: 308px; }
  .cover__photo {
    position: absolute; inset: 0;
    background: radial-gradient(circle at 28% 62%, #dfe8f2 0%, #7f93ab 22%, #3b4656 48%, #1d2129 75%);
  }
  .cover__shapes { position: absolute; inset: 0; }
  .cover__kicker {
    position: absolute; left: 27px; top: 28px;
    font-family: "Oswald", Impact, sans-serif; font-weight: 700;
    font-size: 25px; letter-spacing: -0.3px; color: var(--paper);
  }
  .cover__kicker span { color: var(--ink); }
  .cover__title-block {
    position: absolute; left: 272px; top: 39px; width: 308px; height: 157px;
    background: #0b0b0b; padding: 18px 14px 0 18px;
  }
  .cover__title-big {
    font-family: "Oswald", Impact, sans-serif; font-weight: 700;
    font-size: 51px; line-height: 1; color: var(--paper); letter-spacing: 0.5px;
  }
  .cover__title-sub {
    margin-top: 12px;
    font-family: "Oswald", Impact, sans-serif; font-weight: 500;
    font-size: 23px; line-height: 1.2; color: var(--paper); text-transform: uppercase;
  }
  .cover__title-band {
    position: absolute; left: 272px; top: 196px; width: 308px; height: 112px;
    background: linear-gradient(90deg, var(--deep-red) 0%, var(--brand-red) 40%);
    padding: 16px 14px 0 18px;
  }
  .cover__title-small {
    font-family: "Oswald", Impact, sans-serif; font-weight: 500;
    font-size: 25px; line-height: 1.1; color: var(--paper);
  }
  .cover__title-end {
    font-family: "Oswald", Impact, sans-serif; font-weight: 700;
    font-size: 34px; line-height: 1.25; color: var(--paper); letter-spacing: 0.3px;
    white-space: nowrap;
  }

  /* Steps */
  .tip { position: absolute; }
  .page--left .tip { left: 26px; width: 600px; padding-right: 80px; }
  .page--right .tip { left: 28px; width: 530px; }
  .tip__heading {
    font-family: "Oswald", Impact, sans-serif; font-weight: 700;
    font-size: 20px; line-height: 1.2; color: var(--brand-red);
    display: flex; gap: 6px; margin-bottom: 10px;
  }
  .tip__number { color: var(--ink); }
  .tip__lead { font-weight: 600; color: var(--ink); font-size: 12.4px; line-height: 16.4px; }
  .tip__body { font-size: 12.4px; line-height: 16.4px; color: var(--body-ink); }
  .page--right .tip__body { text-align: justify; }
  .tip__options {
    margin: 18px 0 0 28px;
    display: grid; grid-template-columns: 232px 1fr; column-gap: 12px;
    font-style: italic; font-size: 12.4px; line-height: 16.4px; color: var(--ink);
    list-style: none;
  }

  /* Footer */
  .footer { position: absolute; left: 0; bottom: 0; width: 580px; height: 70px; }
  .footer__rule { position: absolute; left: 0; top: 0; width: 580px; height: 1px; background: var(--rule); }
  .footer__logo {
    position: absolute; left: 26px; top: 4px; width: 40px; height: 58px;
    background: var(--paper); border: 1px solid #dcdcdc;
    display: flex; flex-direction: column; align-items: center; justify-content: center; gap: 4px;
  }
  .footer__logo-mark { width: 18px; height: 18px; background: var(--brand-red); }
  .footer__logo-name {
    font-family: "Open Sans", Arial, sans-serif; font-weight: 600;
    font-size: 6.5px; line-height: 1.1; color: var(--deep-red); text-align: center;
  }
  .footer__contacts {
    position: absolute; left: 66px; top: 19px; width: 484px; height: 25px;
    background: var(--brand-red);
    display: flex; align-items: center; gap: 14px; padding: 0 8px;
    font-weight: 600; font-size: 10.4px; color: var(--paper); white-space: nowrap;
  }
</style>
</head>
<body>
<main class="spread">

  <section class="page page--left">
    <header class="cover">
      <div class="cover__photo" role="img" aria-label="Stock photo of a businessman in a suit holding a glowing globe with a laptop, tablet and network of connected people icons"></div>
      <svg class="cover__shapes" width="580" height="308" viewBox="0 0 580 308" aria-hidden="true">
        <polygon points="0,0 311,0 0,222" fill="#ec1f27"/>
        <polygon points="260,0 311,0 346,39 272,39" fill="#a50f16"/>
      </svg>
      <p class="cover__kicker"><span>FREE</span> Report:</p>
      <div class="cover__title-block">
        <h1 class="cover__title-big">7 STEPS TO</h1>
        <p class="cover__title-sub">Sharpen Your<br>Sales Pitch</p>
      </div>
      <div class="cover__title-band">
        <p class="cover__title-small">BEFORE</p>
        <p class="cover__title-end">SPRING ARRIVES</p>
      </div>
    </header>

    <article class="tip" style="top:324px">
      <h2 class="tip__heading"><span class="tip__number">1.</span> Review your existing customer database</h2>
      <p class="tip__lead">- can you cross sell other products or services to them?</p>
      <p class="tip__body">It’s much cheaper to sell to your existing customers than try to find new customers. Can you upsell them i.e. to encourage them to purchase either more products, or products on a more frequent basis, or products of a greater total value?</p>
    </article>

    <article class="tip" style="top:443px; left:23px">
      <h2 class="tip__heading"><span class="tip__number">2.</span> Review your value proposition</h2>
      <p class="tip__lead">- i.e. what value do you offer your customers?</p>
      <p class="tip__body">List all the benefits of your products, services and your business offers customers and how these differ from your competitors. Put these benefits in your sales and corporate literature, on your website and in your social media profiles. Make sure your sales team knows these benefits by heart!</p>
    </article>

    <article class="tip" style="top:575px; left:29px">
      <h2 class="tip__heading"><span class="tip__number">3.</span> Get a marketing plan</h2>
      <p class="tip__body">- a list of marketing activity that can be undertaken month-by-month for 12 months. You will be amazed at how quickly you will reach the goals for your business with a marketing plan!</p>
    </article>

    <article class="tip" style="top:676px; left:29px">
      <h2 class="tip__heading"><span class="tip__number">4.</span> Optimise your website</h2>
      <p class="tip__body">to increase the number of visitors to it, in order to increase the probability that people will engage with your business and eventually become customers</p>
    </article>

    <footer class="footer">
      <div class="footer__rule"></div>
      <div class="footer__logo">
        <div class="footer__logo-mark"></div>
        <p class="footer__logo-name">Blue Harbour Marketing</p>
      </div>
      <p class="footer__contacts">
        <span>www.blueharbourmarketing.com</span><span>01632 960 418</span><span>info@blueharbourmarketing.co.uk</span>
      </p>
    </footer>
  </section>

  <section class="page page--right">
    <article class="tip" style="top:37px">
      <h2 class="tip__heading"><span class="tip__number">5.</span> Ensure you have a mobile friendly website</h2>
      <p class="tip__body">website - more people now search the internet via their mobile phone or tablet than a PC or laptop! Research shows that consumers are more likely to buy from a business with a mobile friendly website than one that only has a standard website. And if you don’t sell via the internet, you should - virtually all businesses can benefit massively from a ‘shop on the internet’. Initially, some businesses start via BidBazaar or SwapPost but eventually need their own e-commerce website.</p>
    </article>

    <article class="tip" style="top:215px">
      <h2 class="tip__heading"><span class="tip__number">6.</span> Embrace social media and video</h2>
      <p class="tip__body">it’s here to stay and those businesses, even small and medium-sized businesses, that choose to ignore social media will be left behind in the near future. The number of videos watched on ReelHub and other video channels such as FrameVault will blow your mind, and the benefits are massive: more traffic to your website, a higher profile and greater credibility and authority.</p>
      <ul class="tip__options">
        <li>a. Set up a Friendspace Page (not profile)</li>
        <li>d. Set up a ProLinker Company Profile</li>
        <li>b. Set up a CircleNet Page</li>
        <li>e. Start to use all of the above</li>
        <li>c. Set up a company Chirper account</li>
      </ul>
    </article>

    <article class="tip" style="top:470px">
      <h2 class="tip__heading"><span class="tip__number">7.</span> Commit to regular, professional marketing</h2>
      <p class="tip__body">- image is all. Get your branding, corporate literature, sales literature, exhibition materials and website reviewed - professionally - and re-designed to be congruent with who you are as a company and how you want to position your company in the minds of your existing and potential customers. Then invest time and some resources into regular marketing activity, preferably from a marketing plan. Generally, it’s quicker, easier and far more affordable to outsource your marketing than employ someone in-house, at least initially. You will be surprised how quickly regular, focused marketing brings results.</p>
    </article>

    <footer class="footer">
      <div class="footer__rule"></div>
      <div class="footer__logo">
        <div class="footer__logo-mark"></div>
        <p class="footer__logo-name">Blue Harbour Marketing</p>
      </div>
      <p class="footer__contacts">
        <span>www.blueharbourmarketing.com</span><span>01632 960 418</span><span>info@blueharbourmarketing.co.uk</span>
      </p>
    </footer>
  </section>

</main>
</body>
</html>
```